Food Packaging for Shaved/Snow Ice (frozen dessert)

Need packing design for 7 different flavor shaved ice blocks. Already have company logo and feature product elements. Need to incorporate logo and featured elements into the packaging design.
The company name in Hokkien language means flipping table which is incorporated in the company logo and featured products. There are total of 7 flavor products that needs design work, mango, strawberry, pineapple, milk tea, coffee, red bean and peanuts. The goal is to have a common packaging theme for all the flavors and incorporate the corresponding feature elements for each flavor.
The eps files are uploaded below. The packaging is a plastic wrapping/pouch type. Packaging size is 11.25cm width x 14cm legnth; on the back size, need to leave 6.9cm width x 7.8 length for food labeling. More info on product and packing can be found in the "product sample clarification.pdf."
Target Market(s)
The intended product audience is 16-35 years of age consumers.
Industry/Entity Type
Food Production
Requirements
Must have
- Incorporate the company logo and corresponding feature product element provided.

```html
<!DOCTYPE html>
<html lang="en">
<head>
<meta charset="utf-8">
<title>Flip Table Ice – Shaved Ice Packaging Set</title>
<link rel="stylesheet" href="https://fonts.googleapis.com/css2?family=Arimo:wght@400;700&family=Archivo+Black&display=swap">
<style>
  :root{
    --ink:#111111;
    --paper:#ffffff;
    --redbean:#5c2a2a;
    --straw-red:#d42236;
    --straw-green:#2a8f45;
    --milktea:#c48e76;
    --mango-yellow:#f8c444;
    --mango-orange:#f3903f;
    --peanut-grey:#d1d0d0;
    --peanut-brown:#9a6a4c;
    --coffee-blue:#6ccbe0;
    --coffee-brown:#6e3f25;
    --pine-green:#2c8b3e;
    --pine-gold:#df9a28;
  }
  *{box-sizing:border-box;margin:0;padding:0}
  html,body{width:958px;height:1200px;overflow:hidden;background:var(--paper)}
  .sheet{position:relative;width:958px;height:1200px;font-family:"Arimo",Arial,sans-serif;color:var(--ink)}

  .panel{position:absolute;width:223px;height:277px;overflow:hidden}
  .c1{left:0}.c2{left:246px}.c3{left:488px}.c4{left:734px}
  .r1{top:0}.r2{top:312px}.r3{top:606px}.r4{top:918px}

  /* brand block */
  .brand-block{position:absolute;left:20px;top:20px;width:240px;height:250px;display:flex;flex-direction:column;align-items:center;justify-content:center;gap:14px}
  .brand-dot{width:26px;height:26px;border:4px solid var(--ink);border-radius:50%}
  .brand-name{font-weight:700;font-size:30px;line-height:1.15;letter-spacing:3px;text-align:center}

  /* front panels */
  .front{background:var(--bg)}
  .front .band{position:absolute;inset:0;background:var(--band);clip-path:polygon(0 0,78% 0,56% 100%,0 100%)}
  .front .band-low{position:absolute;left:0;right:0;bottom:0;height:38%;background:var(--band2,transparent);clip-path:polygon(0 30%,100% 0,100% 100%,0 100%)}
  .front .flavor{position:absolute;top:10px;left:0;width:100%;text-align:center;font-weight:700;font-size:13px;letter-spacing:.3px;color:var(--label,var(--ink))}
  .front .brand{position:absolute;left:26px;top:92px;display:flex;align-items:flex-start;gap:8px}
  .front .brand-dot{width:16px;height:16px;border-width:3px;border-color:var(--mark,var(--ink));margin-top:3px}
  .front .brand-text{font-weight:700;font-size:19px;line-height:1.12;letter-spacing:2px;color:var(--mark,var(--ink))}
  .front .scene{position:absolute;left:100px;top:168px;width:112px;height:100px;border-radius:10px;background:var(--scene)}

  /* back panels */
  .back .pattern{position:absolute;inset:0;background:radial-gradient(circle at 30% 30%,var(--p2) 0,var(--p1) 75%)}
  .facts{position:absolute;left:73px;top:112px;width:140px;height:160px;background:var(--paper);border:4px solid var(--ink);padding:3px 4px;font-size:4.6px;line-height:1.42}
  .facts h3{font-family:"Archivo Black","Arimo",sans-serif;font-weight:400;font-size:11.5px;letter-spacing:1px;line-height:1.1;border-bottom:.6px solid var(--ink)}
  .facts .thick{border-bottom:2.5px solid var(--ink)}
  .facts .row{display:flex;justify-content:space-between;border-bottom:.4px solid var(--ink)}
  .facts .in{padding-left:7px}
  .facts b{font-weight:700}
  .facts .note{margin-top:1px;font-size:4px;line-height:1.3}
  .facts .ref{display:grid;grid-template-columns:2fr 1fr 1fr;font-size:3.8px;line-height:1.3;margin-top:1px}

  /* flavour themes */
  .redbean{--bg:var(--redbean);--band:var(--redbean);--band2:var(--paper);--scene:#c9a9a3;--label:var(--paper);--mark:var(--paper);--p1:var(--paper);--p2:#e6d3d3}
  .strawberry{--bg:var(--straw-red);--band:var(--straw-green);--scene:#f2c9c9;--p1:var(--straw-green);--p2:#4e9a58}
  .milktea{--bg:var(--milktea);--band:var(--paper);--scene:#f1e2da;--p1:var(--paper);--p2:#f1e0d8}
  .mango{--bg:var(--mango-yellow);--band:var(--mango-orange);--scene:#fbe2b8;--p1:var(--mango-yellow);--p2:#f7b040}
  .peanut{--bg:var(--peanut-brown);--band:var(--peanut-grey);--scene:#e6e2df;--p1:var(--peanut-grey);--p2:#c3b4a8}
  .coffee{--bg:var(--coffee-blue);--band:var(--coffee-brown);--scene:#e9e4e1;--mark:var(--paper);--p1:var(--coffee-blue);--p2:#7fb4bd}
  .pineapple{--bg:var(--pine-green);--band:var(--pine-gold);--scene:#f1e3c0;--p1:var(--pine-gold);--p2:#b99a30}
</style>
</head>
<body>
<main class="sheet">

  <section class="brand-block">
    <span class="brand-dot"></span>
    <span class="brand-name">FLIP<br>TABLE<br>ICE</span>
  </section>

  <!-- Red bean -->
  <section class="panel front redbean c3 r1">
    <div class="band"></div><div class="band-low"></div>
    <div class="brand"><span class="brand-dot"></span><p class="brand-text">FLIP<br>TABLE<br>ICE</p></div>
    <div class="scene" role="img" aria-label="Mascot beside a red bean ice block"></div>
    <h2 class="flavor">RED BEAN</h2>
  </section>
  <section class="panel back redbean c4 r1">
    <div class="pattern" role="img" aria-label="Repeating red bean pattern"></div>
    <div class="facts">
      <h3>Nutrition Facts</h3>
      <div>Serving Size 28.4g</div>
      <div class="thick"><b>Amount Per Serving</b><br><b>Calories</b> 60</div>
      <div class="row"><span></span><b>% Daily Values*</b></div>
      <div class="row"><span><b>Total Fat</b> 0g</span><b>0%</b></div>
      <div class="row in"><span>Saturated Fat 0g</span><b>0%</b></div>
      <div class="row in"><span>Trans Fat 0g</span><span></span></div>
      <div class="row"><span><b>Cholesterol</b> 22mg</span><b>7%</b></div>
      <div class="row"><span><b>Sodium</b> 381mg</span><b>16%</b></div>
      <div class="row"><span><b>Total Carbohydrate</b> 1g</span><b>0%</b></div>
      <div class="row in"><span>Dietary Fiber 0g</span><b>0%</b></div>
      <div class="row in"><span>Sugars 1g</span><span></span></div>
      <div class="row thick"><span><b>Protein</b> 13g</span><b>26%</b></div>
      <div>Iron 13%</div>
      <p class="note">*Percent Daily Values are based on a 2,000 calorie diet.</p>
      <div class="ref"><span>Total Fat</span><span>65g</span><span>80g</span><span>Sodium</span><span>2400mg</span><span>2400mg</span><span>Total Carbohydrate</span><span>300g</span><span>375g</span></div>
    </div>
  </section>

  <!-- Strawberry -->
  <section class="panel front strawberry c1 r2">
    <div class="band"></div>
    <div class="brand"><span class="brand-dot"></span><p class="brand-text">FLIP<br>TABLE<br>ICE</p></div>
    <div class="scene" role="img" aria-label="Rabbit mascot beside a strawberry ice block"></div>
    <h2 class="flavor">STRAWBERRY</h2>
  </section>
  <section class="panel back strawberry c2 r2">
    <div class="pattern" role="img" aria-label="Repeating strawberry pattern"></div>
    <div class="facts" style="top:109px">
      <h3>Nutrition Facts</h3>
      <div>Serving Size 28.4g</div>
      <div class="thick"><b>Amount Per Serving</b><br><b>Calories</b> 60</div>
      <div class="row"><span></span><b>% Daily Values*</b></div>
      <div class="row"><span><b>Total Fat</b> 0g</span><b>0%</b></div>
      <div class="row in"><span>Saturated Fat 0g</span><b>0%</b></div>
      <div class="row in"><span>Trans Fat 0g</span><span></span></div>
      <div class="row"><span><b>Cholesterol</b> 22mg</span><b>7%</b></div>
      <div class="row"><span><b>Sodium</b> 381mg</span><b>16%</b></div>
      <div class="row"><span><b>Total Carbohydrate</b> 1g</span><b>0%</b></div>
      <div class="row in"><span>Dietary Fiber 0g</span><b>0%</b></div>
      <div class="row in"><span>Sugars 1g</span><span></span></div>
      <div class="row thick"><span><b>Protein</b> 13g</span><b>26%</b></div>
      <div>Iron 13%</div>
      <p class="note">*Percent Daily Values are based on a 2,000 calorie diet.</p>
      <div class="ref"><span>Total Fat</span><span>65g</span><span>80g</span><span>Sodium</span><span>2400mg</span><span>2400mg</span><span>Total Carbohydrate</span><span>300g</span><span>375g</span></div>
    </div>
  </section>

  <!-- Milk tea -->
  <section class="panel front milktea c3 r2">
    <div class="band"></div>
    <div class="brand"><span class="brand-dot"></span><p class="brand-text">FLIP<br>TABLE<br>ICE</p></div>
    <div class="scene" role="img" aria-label="Mascot beside a milk tea ice block"></div>
    <h2 class="flavor">MILK TEA</h2>
  </section>
  <section class="panel back milktea c4 r2">
    <div class="pattern" role="img" aria-label="Repeating teacup pattern"></div>
    <div class="facts">
      <h3>Nutrition Facts</h3>
      <div>Serving Size 28.4g</div>
      <div class="thick"><b>Amount Per Serving</b><br><b>Calories</b> 60</div>
      <div class="row"><span></span><b>% Daily Values*</b></div>
      <div class="row"><span><b>Total Fat</b> 0g</span><b>0%</b></div>
      <div class="row in"><span>Saturated Fat 0g</span><b>0%</b></div>
      <div class="row in"><span>Trans Fat 0g</span><span></span></div>
      <div class="row"><span><b>Cholesterol</b> 22mg</span><b>7%</b></div>
      <div class="row"><span><b>Sodium</b> 381mg</span><b>16%</b></div>
      <div class="row"><span><b>Total Carbohydrate</b> 1g</span><b>0%</b></div>
      <div class="row in"><span>Dietary Fiber 0g</span><b>0%</b></div>
      <div class="row in"><span>Sugars 1g</span><span></span></div>
      <div class="row thick"><span><b>Protein</b> 13g</span><b>26%</b></div>
      <div>Iron 13%</div>
      <p class="note">*Percent Daily Values are based on a 2,000 calorie diet.</p>
      <div class="ref"><span>Total Fat</span><span>65g</span><span>80g</span><span>Sodium</span><span>2400mg</span><span>2400mg</span><span>Total Carbohydrate</span><span>300g</span><span>375g</span></div>
    </div>
  </section>

  <!-- Mango -->
  <section class="panel front mango c1 r3">
    <div class="band"></div>
    <div class="brand"><span class="brand-dot"></span><p class="brand-text">FLIP<br>TABLE<br>ICE</p></div>
    <div class="scene" role="img" aria-label="Cat mascot beside a mango ice block"></div>
    <h2 class="flavor">MANGO</h2>
  </section>
  <section class="panel back mango c2 r3">
    <div class="pattern" role="img" aria-label="Repeating mango pattern"></div>
    <div class="facts">
      <h3>Nutrition Facts</h3>
      <div>Serving Size 28.4g</div>
      <div class="thick"><b>Amount Per Serving</b><br><b>Calories</b> 60</div>
      <div class="row"><span></span><b>% Daily Values*</b></div>
      <div class="row"><span><b>Total Fat</b> 0g</span><b>0%</b></div>
      <div class="row in"><span>Saturated Fat 0g</span><b>0%</b></div>
      <div class="row in"><span>Trans Fat 0g</span><span></span></div>
      <div class="row"><span><b>Cholesterol</b> 22mg</span><b>7%</b></div>
      <div class="row"><span><b>Sodium</b> 381mg</span><b>16%</b></div>
      <div class="row"><span><b>Total Carbohydrate</b> 1g</span><b>0%</b></div>
      <div class="row in"><span>Dietary Fiber 0g</span><b>0%</b></div>
      <div class="row in"><span>Sugars 1g</span><span></span></div>
      <div class="row thick"><span><b>Protein</b> 13g</span><b>26%</b></div>
      <div>Iron 13%</div>
      <p class="note">*Percent Daily Values are based on a 2,000 calorie diet.</p>
      <div class="ref"><span>Total Fat</span><span>65g</span><span>80g</span><span>Sodium</span><span>2400mg</span><span>2400mg</span><span>Total Carbohydrate</span><span>300g</span><span>375g</span></div>
    </div>
  </section>

  <!-- Peanut -->
  <section class="panel front peanut c3 r3">
    <div class="band"></div>
    <div class="brand"><span class="brand-dot"></span><p class="brand-text">FLIP<br>TABLE<br>ICE</p></div>
    <div class="scene" role="img" aria-label="Elephant mascot beside a peanut ice block"></div>
    <h2 class="flavor">PEANUT</h2>
  </section>
  <section class="panel back peanut c4 r3">
    <div class="pattern" role="img" aria-label="Repeating peanut pattern"></div>
    <div class="facts">
      <h3>Nutrition Facts</h3>
      <div>Serving Size 28.4g</div>
      <div class="thick"><b>Amount Per Serving</b><br><b>Calories</b> 60</div>
      <div class="row"><span></span><b>% Daily Values*</b></div>
      <div class="row"><span><b>Total Fat</b> 0g</span><b>0%</b></div>
      <div class="row in"><span>Saturated Fat 0g</span><b>0%</b></div>
      <div class="row in"><span>Trans Fat 0g</span><span></span></div>
      <div class="row"><span><b>Cholesterol</b> 22mg</span><b>7%</b></div>
      <div class="row"><span><b>Sodium</b> 381mg</span><b>16%</b></div>
      <div class="row"><span><b>Total Carbohydrate</b> 1g</span><b>0%</b></div>
      <div class="row in"><span>Dietary Fiber 0g</span><b>0%</b></div>
      <div class="row in"><span>Sugars 1g</span><span></span></div>
      <div class="row thick"><span><b>Protein</b> 13g</span><b>26%</b></div>
      <div>Iron 13%</div>
      <p class="note">*Percent Daily Values are based on a 2,000 calorie diet.</p>
      <div class="ref"><span>Total Fat</span><span>65g</span><span>80g</span><span>Sodium</span><span>2400mg</span><span>2400mg</span><span>Total Carbohydrate</span><span>300g</span><span>375g</span></div>
    </div>
  </section>

  <!-- Coffee -->
  <section class="panel front coffee c1 r4">
    <div class="band"></div>
    <div class="brand"><span class="brand-dot"></span><p class="brand-text">FLIP<br>TABLE<br>ICE</p></div>
    <div class="scene" role="img" aria-label="Rabbit mascot beside a coffee ice block"></div>
    <h2 class="flavor">COFFEE</h2>
  </section>
  <section class="panel back coffee c2 r4">
    <div class="pattern" role="img" aria-label="Repeating coffee bean pattern"></div>
    <div class="facts" style="top:118px;left:70px">
      <h3>Nutrition Facts</h3>
      <div>Serving Size 28.4g</div>
      <div class="thick"><b>Amount Per Serving</b><br><b>Calories</b> 60</div>
      <div class="row"><span></span><b>% Daily Values*</b></div>
      <div class="row"><span><b>Total Fat</b> 0g</span><b>0%</b></div>
      <div class="row in"><span>Saturated Fat 0g</span><b>0%</b></div>
      <div class="row in"><span>Trans Fat 0g</span><span></span></div>
      <div class="row"><span><b>Cholesterol</b> 22mg</span><b>7%</b></div>
      <div class="row"><span><b>Sodium</b> 381mg</span><b>16%</b></div>
      <div class="row"><span><b>Total Carbohydrate</b> 1g</span><b>0%</b></div>
      <div class="row in"><span>Dietary Fiber 0g</span><b>0%</b></div>
      <div class="row in"><span>Sugars 1g</span><span></span></div>
      <div class="row thick"><span><b>Protein</b> 13g</span><b>26%</b></div>
      <div>Iron 13%</div>
      <p class="note">*Percent Daily Values are based on a 2,000 calorie diet.</p>
      <div class="ref"><span>Total Fat</span><span>65g</span><span>80g</span><span>Sodium</span><span>2400mg</span><span>2400mg</span><span>Total Carbohydrate</span><span>300g</span><span>375g</span></div>
    </div>
  </section>

  <!-- Pineapple -->
  <section class="panel front pineapple c3 r4">
    <div class="band"></div>
    <div class="brand"><span class="brand-dot"></span><p class="brand-text">FLIP<br>TABLE<br>ICE</p></div>
    <div class="scene" role="img" aria-label="Monkey mascot beside a pineapple ice block"></div>
    <h2 class="flavor">PINEAPPLE</h2>
  </section>
  <section class="panel back pineapple c4 r4">
    <div class="pattern" role="img" aria-label="Repeating pineapple pattern"></div>
    <div class="facts">
      <h3>Nutrition Facts</h3>
      <div>Serving Size 28.4g</div>
      <div class="thick"><b>Amount Per Serving</b><br><b>Calories</b> 60</div>
      <div class="row"><span></span><b>% Daily Values*</b></div>
      <div class="row"><span><b>Total Fat</b> 0g</span><b>0%</b></div>
      <div class="row in"><span>Saturated Fat 0g</span><b>0%</b></div>
      <div class="row in"><span>Trans Fat 0g</span><span></span></div>
      <div class="row"><span><b>Cholesterol</b> 22mg</span><b>7%</b></div>
      <div class="row"><span><b>Sodium</b> 381mg</span><b>16%</b></div>
      <div class="row"><span><b>Total Carbohydrate</b> 1g</span><b>0%</b></div>
      <div class="row in"><span>Dietary Fiber 0g</span><b>0%</b></div>
      <div class="row in"><span>Sugars 1g</span><span></span></div>
      <div class="row thick"><span><b>Protein</b> 13g</span><b>26%</b></div>
      <div>Iron 13%</div>
      <p class="note">*Percent Daily Values are based on a 2,000 calorie diet.</p>
      <div class="ref"><span>Total Fat</span><span>65g</span><span>80g</span><span>Sodium</span><span>2400mg</span><span>2400mg</span><span>Total Carbohydrate</span><span>300g</span><span>375g</span></div>
    </div>
  </section>

</main>
</body>
</html>
```